Pipelining Product Supply Company Needs New Stationery

We need new stationery (letter head, with compliments slips & business card) for our industry leading pipe lining supply company. basically we sell product to other plumbers to carry out pipe relining.

Im looking for something, fresh, professional, sleek and modern at the same time.

Ive attached a copy of the logo and also some guidelines to follow for colours and fonts etc.

Target Market(s)

Plumbers

Industry/Entity Type

Plumbing

Font styles to use
Sans Serif

Requirements
Must have
• The logo, space for ABN, Address, Phone Number, website and email.
Nice to have
• Stand out from the crowd. To look sleep and professional.
Should not have
• Any other colours apart from what is on the guidelines.

```html
<!DOCTYPE html>
<html lang="en">
<head>
<meta charset="utf-8">
<title>Kestrel Relining Supplies – Stationery</title>
<link href="https://fonts.googleapis.com/css2?family=Open+Sans:wght@300;400;600;700&display=swap" rel="stylesheet">
<style>
  :root{
    --bg:#333333;
    --paper:#f7f7f7;
    --green-dark:#0d4a12;
    --green-mid:#2c7d1f;
    --green-light:#8cc63f;
    --text:#555555;
    --text-soft:#777777;
  }
  *{box-sizing:border-box;margin:0;padding:0}
  html,body{width:1200px;height:1200px;overflow:hidden;background:var(--bg);font-family:"Open Sans",sans-serif;color:var(--text)}
  .canvas{position:relative;width:1200px;height:1200px}
  .sheet{position:absolute;background:var(--paper);overflow:hidden;box-shadow:0 8px 24px rgba(0,0,0,.35)}
  .icon{width:10px;height:10px;fill:var(--green-light);flex:none}
  .contact-list{list-style:none;display:flex;flex-direction:column;gap:2px}
  .contact-list li{display:flex;align-items:center;gap:5px}
  .brand{display:flex;flex-direction:column;line-height:1}
  .brand-mark{display:flex;align-items:center;gap:8px}
  .brand-square{background:var(--green-mid);flex:none}
  .brand-name{font-weight:700;color:var(--green-mid);letter-spacing:2px}
  .brand-sub{font-weight:300;color:var(--text-soft);text-transform:uppercase}
  .brand-abn{font-weight:300;color:var(--text-soft)}
  .footer-bands{position:absolute;left:0;bottom:0;width:100%;display:block}

  /* Letterhead */
  .letterhead{left:640px;top:180px;width:520px;height:735px}
  .letterhead .contact-list{position:absolute;right:36px;top:34px;font-size:10px}
  .letterhead .brand{position:absolute;left:44px;top:150px}
  .letterhead .brand-square{width:26px;height:26px}
  .letterhead .brand-name{font-size:34px}
  .letterhead .brand-sub{font-size:11px;margin-top:6px}
  .letterhead .brand-abn{font-size:11px;margin-top:4px}
  .letter-body{position:absolute;left:44px;right:40px;top:262px;font-size:9.5px;line-height:1.65}
  .letter-body p{margin-bottom:12px}
  .addressee{margin-bottom:18px}
  .signoff{margin-top:22px}
  .signature{font-size:14px;color:#333;margin-top:4px}

  /* Business card front */
  .card-front{left:40px;top:180px;width:400px;height:230px}
  .card-front .brand{position:absolute;right:26px;top:24px;align-items:flex-end}
  .card-front .brand-square{width:18px;height:18px}
  .card-front .brand-name{font-size:26px}
  .card-front .brand-sub{font-size:8px;margin-top:4px}
  .name-band{position:absolute;left:0;top:74px;width:190px;height:30px;background:var(--green-dark);color:#fff;display:flex;align-items:center;padding-left:20px;font-size:12px;gap:6px}
  .name-band .role{font-size:8px;font-weight:300;opacity:.85;border-left:1px solid #fff;padding-left:6px}
  .card-front .contact-list{position:absolute;left:22px;top:124px;font-size:7.5px}
  .card-front .address{position:absolute;right:26px;top:124px;font-size:7.5px;text-align:right;display:flex;gap:5px}

  /* Business card back */
  .card-back{left:40px;top:440px;width:400px;height:230px;background:radial-gradient(circle at 50% 45%,#5fae2e 0%,var(--green-mid) 45%,var(--green-dark) 100%);display:flex;align-items:center;justify-content:center}
  .card-back .brand-square{width:28px;height:28px;background:var(--green-light)}
  .card-back .brand-name{font-size:52px;color:var(--green-light)}

  /* Compliments slip */
  .slip{left:40px;top:700px;width:540px;height:255px}
  .slip .brand{position:absolute;left:28px;top:30px}
  .slip .brand-square{width:22px;height:22px}
  .slip .brand-name{font-size:30px}
  .slip .brand-sub{font-size:10px;margin-top:5px}
  .slip .brand-abn{font-size:10px;margin-top:3px}
  .slip-title{position:absolute;right:40px;top:56px;font-size:30px;font-weight:400;color:var(--green-light);letter-spacing:-.5px}
  .slip-contacts{position:absolute;left:28px;top:170px;display:flex;gap:14px;font-size:10px}
  .slip-contacts .address{border-left:1px solid #aaa;padding-left:12px;display:flex;gap:5px}
</style>
</head>
<body>
<svg width="0" height="0" style="position:absolute">
  <defs>
    <symbol id="i-phone" viewBox="0 0 24 24"><path d="M6.6 10.8a15 15 0 0 0 6.6 6.6l2.2-2.2a1 1 0 0 1 1-.25 11.4 11.4 0 0 0 3.6.57 1 1 0 0 1 1 1V20a1 1 0 0 1-1 1A17 17 0 0 1 3 4a1 1 0 0 1 1-1h3.5a1 1 0 0 1 1 1c0 1.25.2 2.45.57 3.6a1 1 0 0 1-.25 1z"/></symbol>
    <symbol id="i-web" viewBox="0 0 24 24"><path d="M12 2a10 10 0 1 0 0 20 10 10 0 0 0 0-20zm6.9 6h-3a15.6 15.6 0 0 0-1.4-3.6A8 8 0 0 1 18.9 8zM12 4c.8 1.2 1.5 2.5 1.9 4h-3.8c.4-1.5 1.1-2.8 1.9-4zM4.3 14a8 8 0 0 1 0-4h3.4a16 16 0 0 0 0 4zm.8 2h3a15.6 15.6 0 0 0 1.4 3.6A8 8 0 0 1 5.1 16zm3-8h-3a8 8 0 0 1 4.4-3.6A15.6 15.6 0 0 0 8.1 8zM12 20c-.8-1.2-1.5-2.5-1.9-4h3.8c-.4 1.5-1.1 2.8-1.9 4zm2.3-6H9.7a14.6 14.6 0 0 1 0-4h4.6a14.6 14.6 0 0 1 0 4zm.2 5.6a15.6 15.6 0 0 0 1.4-3.6h3a8 8 0 0 1-4.4 3.6zm1.8-5.6a16 16 0 0 0 0-4h3.4a8 8 0 0 1 0 4z"/></symbol>
    <symbol id="i-mail" viewBox="0 0 24 24"><path d="M20 4H4a2 2 0 0 0-2 2v12a2 2 0 0 0 2 2h16a2 2 0 0 0 2-2V6a2 2 0 0 0-2-2zm0 4-8 5-8-5V6l8 5 8-5z"/></symbol>
    <symbol id="i-pin" viewBox="0 0 24 24"><path d="M12 2a7 7 0 0 0-7 7c0 5.25 7 13 7 13s7-7.75 7-13a7 7 0 0 0-7-7zm0 9.5A2.5 2.5 0 1 1 12 6.5a2.5 2.5 0 0 1 0 5z"/></symbol>
  </defs>
</svg>

<main class="canvas">

  <!-- Letterhead -->
  <section class="sheet letterhead" aria-label="Letterhead">
    <ul class="contact-list">
      <li><svg class="icon"><use href="#i-phone"/></svg>123-456-7890</li>
      <li><svg class="icon"><use href="#i-web"/></svg>www.kestrelrelining.com</li>
      <li><svg class="icon"><use href="#i-mail"/></svg>sam@kestrelrelining.com</li>
      <li><svg class="icon"><use href="#i-pin"/></svg>Dummy city<br>Dummy country, land</li>
    </ul>
    <div class="brand">
      <div class="brand-mark"><span class="brand-square"></span><span class="brand-name">KRS</span></div>
      <span class="brand-sub">Kestrel Relining Supplies</span>
      <span class="brand-abn">ABN. xxx-xxxx-xxxx</span>
    </div>
    <div class="letter-body">
      <p class="addressee">To<br>The, Director</p>
      <p>Lorem ipsum dolor sit amet, consectetur adipiscing elit. Sed at ante. Mauris eleifend, quam a vulputate dictum, massa quam dapibus leo, eget vulputate orci purus ut lorem. In fringilla mi in ligula. Pellentesque aliquam quam vel dolor. Nunc adipiscing. Sed quamodio, tempus ac, aliquam molestie varius ac, tellus. Vestibulum ut nulla aliquam risus rutrum interdum. Pellentesque lorem.</p>
      <p>Curabitur sit amet erat quis risus feugiat viverra. Pellentesque augue justo, sagittis et, lacinia at, venenatis non, arcu. Nunc nec libero. In cursus dictum risus. Etiam tristique nisl a nulla. Ut a orci. Curabitur dolor nunc, egestas at, accumsan at, malesuada nec, magna. Nulla facilisi. Nunc volutpat. Vestibulum ante ipsum primis in faucibus orci luctus et ultrices posuere cubilia Curae; Ut sit amet orci vel mauris blandit vehicula. Nullam quis enim. Integer dignissim viverra velit. Curabitur in odio.</p>
      <p>Curabitur sit amet erat quis risus feugiat viverra. Pellentesque augue justo, sagittis et, lacinia at, venenatis non, arcu. Nunc nec libero. In cursus dictum risus. Etiam tristique nisl a nulla. Ut a orci. Curabitur dolor nunc, egestas at, accumsan at, malesuada nec, magna. Nulla facilisi. Nunc volutpat. Vestibulum ante ipsum primis in faucibus orci luctus et ultrices posuere cubilia Curae; Ut sit amet orci vel mauris blandit vehicula. Nullam quis enim. Integer dignissim viverra velit. Curabitur in odio.</p>
      <p class="signoff">Thank you,</p>
      <p class="signature">Sam Carter</p>
    </div>
    <svg class="footer-bands" viewBox="0 0 520 44" preserveAspectRatio="none" height="44">
      <polygon points="312,0 520,0 520,14 300,14" fill="var(--green-dark)"/>
      <polygon points="0,26 286,26 300,17 520,17 520,44 0,44" fill="var(--green-light)"/>
    </svg>
  </section>

  <!-- Business card front -->
  <section class="sheet card-front" aria-label="Business card front">
    <div class="brand">
      <div class="brand-mark"><span class="brand-square"></span><span class="brand-name">KRS</span></div>
      <span class="brand-sub">Kestrel Relining Supplies</span>
    </div>
    <div class="name-band">SAM CARTER <span class="role">Director</span></div>
    <ul class="contact-list">
      <li>ABN. xxx-xxxx-xxxx</li>
      <li><svg class="icon"><use href="#i-phone"/></svg>123-456-7890</li>
      <li><svg class="icon"><use href="#i-web"/></svg>www.kestrelrelining.com</li>
      <li><svg class="icon"><use href="#i-mail"/></svg>sam@kestrelrelining.com</li>
    </ul>
    <div class="address"><span>Dummy city<br>Dummy country, land</span><svg class="icon"><use href="#i-pin"/></svg></div>
    <svg class="footer-bands" viewBox="0 0 400 36" preserveAspectRatio="none" height="36">
      <polygon points="250,0 400,0 400,12 238,12" fill="var(--green-dark)"/>
      <polygon points="0,22 226,22 238,14 400,14 400,36 0,36" fill="var(--green-light)"/>
    </svg>
  </section>

  <!-- Business card back -->
  <section class="sheet card-back" aria-label="Business card back">
    <div class="brand-mark"><span class="brand-square"></span><span class="brand-name">KRS</span></div>
  </section>

  <!-- Compliments slip -->
  <section class="sheet slip" aria-label="With compliments slip">
    <div class="brand">
      <div class="brand-mark"><span class="brand-square"></span><span class="brand-name">KRS</span></div>
      <span class="brand-sub">Kestrel Relining Supplies</span>
      <span class="brand-abn">ABN. xxx-xxxx-xxxx</span>
    </div>
    <h1 class="slip-title">WITH COMPLIMENTS</h1>
    <div class="slip-contacts">
      <ul class="contact-list">
        <li><svg class="icon"><use href="#i-phone"/></svg>123-456-7890</li>
        <li><svg class="icon"><use href="#i-web"/></svg>www.kestrelrelining.com</li>
        <li><svg class="icon"><use href="#i-mail"/></svg>sam@kestrelrelining.com</li>
      </ul>
      <div class="address"><svg class="icon"><use href="#i-pin"/></svg><span>Dummy city<br>Dummy country, land</span></div>
    </div>
    <svg class="footer-bands" viewBox="0 0 540 40" preserveAspectRatio="none" height="40">
      <polygon points="336,0 540,0 540,13 324,13" fill="var(--green-dark)"/>
      <polygon points="0,24 310,24 324,15 540,15 540,40 0,40" fill="var(--green-light)"/>
    </svg>
  </section>

</main>
</body>
</html>
```